Pediatric Dental Practice needs a postcard for direct mail advertising

We are looking for a creative and professional double-sided postcard design for a direct mail marketing campaign. Our goal is to attract new families to our pediatric dental practice by conveying a sense of warmth, modern care, and clinical excellence. The design should feel "boutique" and high-end yet remain fun and approachable for parents and children.

```html
<!DOCTYPE html>
<html lang="en">
<head>
<meta charset="UTF-8">
<title>Maple Grove Pediatric Dentistry – Postcard</title>
<link rel="stylesheet" href="https://fonts.googleapis.com/css2?family=Open+Sans:wght@300;400;500;600;700&display=swap">
<style>
  :root {
    --green: #2e9957;
    --green-dark: #23844a;
    --green-soft: #bfe5c8;
    --ink: #2f3234;
    --ink-soft: #55595c;
    --band: #3a3d3f;
    --paper: #ffffff;
    --backdrop: #eeeeee;
    --photo-light: #eef2f4;
    --photo-mid: #cfdce2;
  }
  * { box-sizing: border-box; margin: 0; padding: 0; }
  html, body {
    width: 1200px; height: 412px; overflow: hidden;
    background: var(--backdrop);
    font-family: "Open Sans", sans-serif;
    color: var(--ink);
  }
  .postcard {
    position: absolute; top: 13px;
    width: 577px; height: 384px;
    background: var(--paper);
    overflow: hidden;
    box-shadow: 0 1px 4px rgba(0,0,0,0.15);
  }
  .postcard--front { left: 16px; }
  .postcard--back { left: 607px; }

  /* ---------- Front ---------- */
  .brand { position: absolute; left: 20px; top: 12px; text-align: center; width: 98px; }
  .brand__dot { width: 30px; height: 30px; border-radius: 50%; background: var(--green-soft); margin: 0 auto 6px; }
  .brand__name { font-size: 16px; font-weight: 500; color: var(--ink); line-height: 1; white-space: nowrap; }
  .brand__sub { font-size: 5.6px; letter-spacing: 1.6px; color: var(--ink); margin-top: 3px; white-space: nowrap; }

  .headline { position: absolute; left: 20px; top: 86px; font-size: 28px; line-height: 33px; font-weight: 400; color: var(--ink); }
  .headline strong, .back-title strong { color: var(--green); font-weight: 700; }
  .rule { position: absolute; height: 2px; background: var(--green); }
  .front-rule { left: 21px; top: 154px; width: 89px; }

  .intro { position: absolute; left: 21px; top: 165px; width: 240px; font-size: 10px; line-height: 15.5px; color: var(--ink-soft); }

  .features { position: absolute; left: 19px; top: 210px; list-style: none; }
  .feature { display: flex; align-items: center; height: 30px; margin-bottom: 8.5px; }
  .feature__icon { width: 30px; height: 30px; border-radius: 50%; background: var(--green); display: flex; align-items: center; justify-content: center; }
  .feature:nth-child(2) .feature__icon, .feature:nth-child(4) .feature__icon { background: #4fae6f; }
  .feature__label { margin-left: 13px; font-size: 10px; color: var(--ink); letter-spacing: 0.1px; }

  .photo { position: absolute; right: 0; top: 0; width: 330px; height: 384px; }

  /* ---------- Back ---------- */
  .back-title { position: absolute; left: 20px; top: 12px; font-size: 27px; line-height: 32px; font-weight: 400; color: var(--ink); }
  .back-title strong { font-weight: 600; }
  .back-rule { left: 22px; top: 84px; width: 88px; }
  .back-intro { position: absolute; left: 22px; top: 97px; width: 250px; font-size: 10px; line-height: 15.5px; color: var(--ink-soft); }

  .offer-ribbon {
    position: absolute; left: 25px; top: 137px; width: 168px; height: 23px;
    background: var(--band); color: #fff; font-size: 9.5px; font-weight: 700;
    display: flex; align-items: center; justify-content: center; letter-spacing: 0.2px;
    clip-path: polygon(0 0, 100% 0, 94% 50%, 100% 100%, 0 100%, 4% 50%);
  }
  .offer-link { position: absolute; left: 185px; top: 140px; width: 80px; height: 20px; }
  .offer-badge {
    position: absolute; left: 227px; top: 146px; width: 70px; height: 70px; border-radius: 50%;
    background: var(--green-soft); display: flex; flex-direction: column; align-items: center; justify-content: center;
    color: #1b1d1e; font-weight: 700; line-height: 1;
  }
  .offer-badge__amount { font-size: 17px; }
  .offer-badge__unit { font-size: 12px; margin-top: 3px; }
  .offer-detail { position: absolute; left: 27px; top: 168px; font-size: 11px; color: var(--ink); }
  .gift-title { position: absolute; left: 27px; top: 195px; font-size: 17px; font-weight: 500; color: var(--green); }
  .gift-detail { position: absolute; left: 29px; top: 220px; font-size: 9.2px; color: var(--ink); }
  .gift-rule { left: 25px; top: 253px; width: 178px; height: 1.5px; }
  .gift-art { position: absolute; left: 215px; top: 238px; width: 52px; height: 52px; border-radius: 6px; background: #e7f4eb; }

  .contacts { position: absolute; left: 24px; top: 275px; list-style: none; }
  .contact { display: flex; align-items: center; height: 19px; margin-bottom: 9.5px; }
  .contact__icon { width: 19px; height: 19px; border-radius: 50%; background: var(--green); display: flex; align-items: center; justify-content: center; }
  .contact__text { margin-left: 14px; font-size: 11px; color: var(--ink); }

  .social-band { position: absolute; left: 0; bottom: 0; width: 300px; height: 20px; background: var(--band); }
  .social-band__label { position: absolute; left: 26px; top: 3px; font-size: 10px; font-weight: 700; color: #fff; }
  .social-band__dots { position: absolute; left: 233px; top: 4px; display: flex; gap: 4px; }
  .social-band__dots span { width: 12px; height: 12px; border-radius: 50%; background: #fff; }

  .mail-panel { position: absolute; right: 0; top: 0; width: 300px; height: 384px; }
  .mail-brand { position: absolute; left: 307px; top: 26px; width: 88px; text-align: center; color: #fff; }
  .mail-brand__dot { width: 26px; height: 26px; border-radius: 50%; border: 2px solid #fff; margin: 0 auto 5px; }
  .mail-brand__name { font-size: 13.5px; font-weight: 500; line-height: 1; white-space: nowrap; }
  .mail-brand__sub { font-size: 4.8px; letter-spacing: 1.3px; margin-top: 2px; white-space: nowrap; }
  .stamp-box { position: absolute; left: 504px; top: 20px; width: 55px; height: 61px; border: 1px dashed rgba(255,255,255,0.9); }
  .address-line { position: absolute; left: 349px; width: 210px; border-top: 1px dotted rgba(255,255,255,0.9); }
</style>
</head>
<body>

<section class="postcard postcard--front">
  <div class="brand">
    <div class="brand__dot"></div>
    <div class="brand__name">Maple Grove</div>
    <div class="brand__sub">PEDIATRIC DENTISTRY</div>
  </div>

  <h1 class="headline">Growing <strong>Healthy</strong><br><strong>Smiles</strong> Together</h1>
  <div class="rule front-rule"></div>
  <p class="intro">Specialised dental care for children in a warm, fun and friendly environment.</p>

  <ul class="features">
    <li class="feature">
      <span class="feature__icon"><svg width="16" height="16" viewBox="0 0 16 16" fill="none" stroke="#fff" stroke-width="1.3"><circle cx="8" cy="8" r="6.2"/><path d="M5.2 9.5c1.5 1.6 4.1 1.6 5.6 0" stroke-linecap="round"/><circle cx="5.8" cy="6.3" r="0.5" fill="#fff"/><circle cx="10.2" cy="6.3" r="0.5" fill="#fff"/></svg></span>
      <span class="feature__label">CHILD FOCUSED CARE</span>
    </li>
    <li class="feature">
      <span class="feature__icon"><svg width="16" height="16" viewBox="0 0 16 16" fill="none" stroke="#fff" stroke-width="1.3" stroke-linejoin="round"><path d="M8 1.8l5 2v4c0 3-2.2 5.2-5 6.4-2.8-1.2-5-3.4-5-6.4v-4z"/><path d="M5.6 8l1.7 1.7 3.2-3.3" stroke-linecap="round"/></svg></span>
      <span class="feature__label">PREVENTIVE &amp; GENTLE</span>
    </li>
    <li class="feature">
      <span class="feature__icon"><svg width="16" height="16" viewBox="0 0 16 16" fill="none" stroke="#fff" stroke-width="1.3" stroke-linejoin="round"><path d="M4 3c1.5-.8 2.6 0 4 0s2.5-.8 4 0c1.4.9.9 3.4.4 5-.5 1.7-.7 5-1.8 5-1 0-1.1-3.3-2.6-3.3S6.6 13 5.6 13c-1.1 0-1.3-3.3-1.8-5C3.3 6.4 2.6 3.9 4 3z"/></svg></span>
      <span class="feature__label">MODERN TECHNOLOGY</span>
    </li>
    <li class="feature">
      <span class="feature__icon"><svg width="16" height="16" viewBox="0 0 16 16" fill="none" stroke="#fff" stroke-width="1.3" stroke-linejoin="round"><path d="M8 13.5S2.5 10.2 2.5 6.3C2.5 4.5 3.8 3.2 5.4 3.2c1.1 0 2 .6 2.6 1.5.6-.9 1.5-1.5 2.6-1.5 1.6 0 2.9 1.3 2.9 3.1 0 3.9-5.5 7.2-5.5 7.2z"/></svg></span>
      <span class="feature__label">PARENTS WELCOME</span>
    </li>
  </ul>

  <svg class="photo" viewBox="0 0 330 384" role="img" aria-label="Photo of a smiling dentist in blue gloves examining a happy young girl in a dental chair">
    <defs>
      <linearGradient id="photoTone" x1="0" y1="0" x2="1" y2="1">
        <stop offset="0" stop-color="#eef2f4"/>
        <stop offset="0.55" stop-color="#dfe7eb"/>
        <stop offset="1" stop-color="#c6d6de"/>
      </linearGradient>
    </defs>
    <path d="M31 0 C14 25 6 55 10 80 C16 120 60 150 55 186 C50 225 4 265 6 312 C7 345 20 368 31 384 L330 384 L330 0 Z" fill="url(#photoTone)"/>
    <path d="M31 0 C14 25 6 55 10 80 C16 120 60 150 55 186 C50 225 4 265 6 312 C7 345 20 368 31 384" fill="none" stroke="var(--green)" stroke-width="4"/>
  </svg>
</section>

<section class="postcard postcard--back">
  <h2 class="back-title">Trusted Care<br><strong>Bright Smiles</strong></h2>
  <div class="rule back-rule"></div>
  <p class="back-intro">We partner with parents to make every visit positive, comfortable and rewarding for your child.</p>

  <div class="offer-ribbon">NEW PATIENT OFFER</div>
  <svg class="offer-link" viewBox="0 0 80 20" fill="none"><path d="M2 6 C25 -2 50 2 60 14" stroke="var(--green)" stroke-width="1" stroke-dasharray="1.5 2"/></svg>
  <div class="offer-badge"><span class="offer-badge__amount">$50</span><span class="offer-badge__unit">OFF</span></div>
  <p class="offer-detail">your child's first visit!</p>

  <p class="gift-title">Complimentary</p>
  <p class="gift-detail">Kids Oral Health Pack with every new patient visit.</p>
  <div class="rule gift-rule"></div>
  <div class="gift-art" role="img" aria-label="Line illustration of a toothpaste tube, a tooth and a toothbrush"></div>

  <ul class="contacts">
    <li class="contact">
      <span class="contact__icon"><svg width="10" height="10" viewBox="0 0 10 10"><path d="M2.2 1c.4 0 1.4 1.6 1.4 2 0 .5-.8.8-.7 1.2.3.9 1.1 1.8 2 2.1.4.1.7-.7 1.2-.7.4 0 2 1 2 1.4 0 .7-1 1.6-1.8 1.5C3.7 8.2 1.6 6 1 3.1.9 2.2 1.5 1 2.2 1z" fill="#fff"/></svg></span>
      <span class="contact__text">(02) 5550 1234</span>
    </li>
    <li class="contact">
      <span class="contact__icon"><svg width="10" height="10" viewBox="0 0 10 10"><path d="M5 .8C3.2.8 1.9 2.1 1.9 3.8 1.9 6 5 9.3 5 9.3S8.1 6 8.1 3.8C8.1 2.1 6.8.8 5 .8z" fill="#fff"/><circle cx="5" cy="3.8" r="1.2" fill="var(--green)"/></svg></span>
      <span class="contact__text">48 Bright Lane, Sunnyvale NSW 2000</span>
    </li>
    <li class="contact">
      <span class="contact__icon"><svg width="11" height="11" viewBox="0 0 12 12" fill="none" stroke="#fff" stroke-width="0.9"><circle cx="6" cy="6" r="4.6"/><ellipse cx="6" cy="6" rx="2" ry="4.6"/><path d="M1.4 6h9.2M2 3.8h8M2 8.2h8"/></svg></span>
      <span class="contact__text">www.maplegrovekids.com.au</span>
    </li>
  </ul>

  <div class="social-band">
    <span class="social-band__label">Follow US</span>
    <div class="social-band__dots"><span></span><span></span><span></span></div>
  </div>

  <svg class="mail-panel" viewBox="0 0 300 384" aria-hidden="true">
    <path d="M20 0 C8 25 -4 55 0 80 C8 120 48 150 44 191 C40 235 -4 270 -2 312 C-1 345 10 368 17 384 L300 384 L300 0 Z" fill="var(--green)"/>
  </svg>

  <div class="mail-brand">
    <div class="mail-brand__dot"></div>
    <div class="mail-brand__name">Maple Grove</div>
    <div class="mail-brand__sub">PEDIATRIC DENTISTRY</div>
  </div>
  <div class="stamp-box"></div>
  <div class="address-line" style="top:187px"></div>
  <div class="address-line" style="top:219px"></div>
  <div class="address-line" style="top:251px"></div>
  <div class="address-line" style="top:283px"></div>
  <div class="address-line" style="top:315px"></div>
</section>

</body>
</html>
```